DORV2020 Save the date post card

Take the look and feel of the logo you designed and create a save the date postcard. 7L" by 5"H - print ready file with crop marks and bleeds.

Colors

Designer to choose colors to be used in the design.

Requirements
Must have
• The logo somewhere on the card.
• The following text:
• Save the Date
• June 1 - 4
• dorvsummit.ca
• Stronger United: Gather. Spark. Flourish.
Nice to have
• The following text:
• Vision: The vision of the DORV 2020 conference is to improve patient care by bringing together the Canadian Emergency Medicine community.
• Learning Objectives:
• By the end of the conference, delegates will be able to;
• • Apply up to date evidence to inform clinical decisions;
• • Acquire practical skills by participating in interactive sessions;
• • Connect and collaborate with other delegates;
• • Consider strategies to ensure career longevity; and
• • Influence the future direction of Emergency Medicine in Canada

```html
<!DOCTYPE html>
<html lang="en">
<head>
<meta charset="utf-8">
<title>DORV2020 Save the Date Postcard</title>
<link href="https://fonts.googleapis.com/css2?family=Oswald:wght@500;700&family=Open+Sans:wght@400;600;700&display=swap" rel="stylesheet">
<style>
  :root {
    --navy: #0f2a5c;
    --navy-deep: #0a1e44;
    --blue: #1f5fae;
    --purple: #7b2f9e;
    --magenta: #b03bb0;
    --white: #ffffff;
    --page: #ececec;
    --sky: #8fb6d9;
    --green: #5f8a4a;
    --stone: #b9a88a;
  }
  * { box-sizing: border-box; margin: 0; padding: 0; }
  html, body { width: 878px; height: 1200px; overflow: hidden; }
  body { background: var(--page); font-family: "Open Sans", Arial, sans-serif; position: relative; }

  .postcard {
    position: absolute; left: 111px; width: 656px; height: 469px;
    background: var(--white); overflow: hidden;
    box-shadow: 0 4px 14px rgba(0,0,0,.25);
  }
  .postcard--front { top: 70px; }
  .postcard--back { top: 640px; }

  .photo { position: absolute; }
  .photo--city { right: 0; top: 0; width: 470px; height: 330px;
    background: linear-gradient(180deg, var(--sky) 0%, #c7dcec 45%, var(--stone) 62%, var(--green) 78%, #3f6a3a 100%); }
  .photo--round { border-radius: 50%; border: 4px solid var(--white);
    background: linear-gradient(160deg, #c9c2c9, #7a6f86); }
  .photo--lab { left: 0; top: 0; width: 400px; height: 190px;
    background: linear-gradient(160deg, #9aa6b3, #4c5a6a 70%, #2f3d4c); }

  .shapes { position: absolute; left: 0; top: 0; }

  .front-headline { position: absolute; left: 26px; top: 46px; color: var(--white);
    font-family: "Oswald", Arial, sans-serif; font-weight: 700; font-size: 44px; line-height: 1; }
  .front-date { position: absolute; left: 26px; top: 144px; color: var(--white);
    font-family: "Oswald", Arial, sans-serif; font-weight: 500; font-size: 18px; }
  .tagline { position: absolute; color: var(--white); font-family: "Oswald", Arial, sans-serif; font-weight: 500; line-height: 1.1; }
  .front-tagline { left: 26px; top: 224px; font-size: 18px; width: 210px; }
  .front-tagline strong { display: block; font-size: 21px; font-weight: 500; }

  .vision { position: absolute; left: 0; top: 330px; width: 372px; height: 58px;
    background: var(--purple); color: var(--white); font-size: 11px; font-weight: 600;
    line-height: 1.3; padding: 7px 14px 0 26px; }

  .url { position: absolute; font-size: 12px; font-weight: 700; }
  .front-url { left: 20px; top: 410px; color: var(--purple); }
  .url .dot { display: inline-block; width: 9px; height: 9px; border-radius: 50%; background: var(--magenta); margin-right: 6px; }

  .logo { position: absolute; display: flex; align-items: center; gap: 8px;
    font-family: "Open Sans", Arial, sans-serif; font-weight: 700; color: var(--purple); }
  .logo .mark { width: 16px; height: 16px; background: var(--purple); }
  .front-logo { left: 470px; top: 398px; font-size: 26px; }
  .back-logo { left: 430px; top: 86px; font-size: 20px; }

  .objectives { position: absolute; left: 0; top: 230px; width: 330px; height: 128px;
    background: var(--navy); color: var(--white); padding: 12px 14px 0 26px; font-size: 9.5px; line-height: 1.35; }
  .objectives h2 { font-size: 11px; font-weight: 700; }
  .objectives p { font-weight: 600; margin-bottom: 4px; }
  .objectives ul { list-style: none; }
  .objectives li::before { content: "• "; }

  .back-info { position: absolute; left: 0; top: 362px; width: 330px; padding: 8px 0 0 26px; }
  .back-tagline { color: var(--blue); font-family: "Oswald", Arial, sans-serif; font-weight: 500; font-size: 17px; }
  .back-date { color: var(--navy); font-size: 12px; font-weight: 700; margin-top: 8px; }
  .back-url-band { position: absolute; left: 0; top: 432px; width: 250px; height: 24px; background: var(--purple);
    color: var(--white); font-size: 12px; font-weight: 700; padding: 4px 0 0 26px; }
  .back-url-band .dot { display: inline-block; width: 9px; height: 9px; border-radius: 50%; background: var(--white); margin-right: 6px; }
</style>
</head>
<body>

<section class="postcard postcard--front" aria-label="Postcard front">
  <div class="photo photo--city" role="img" aria-label="Photo of the host city skyline with parliament buildings above the river"></div>
  <svg class="shapes" width="656" height="469" viewBox="0 0 656 469" aria-hidden="true">
    <defs>
      <linearGradient id="frontStripe" x1="0" y1="0" x2="1" y2="1">
        <stop offset="0" stop-color="#1f5fae"/>
        <stop offset="1" stop-color="#7b2f9e"/>
      </linearGradient>
    </defs>
    <polygon points="0,0 300,0 250,330 0,330" fill="url(#frontStripe)"/>
    <polygon points="0,0 270,0 222,330 0,330" fill="#0f2a5c"/>
  </svg>
  <div class="photo photo--round" style="left:250px;top:22px;width:74px;height:74px" role="img" aria-label="Round photo of delegates at a session"></div>
  <div class="photo photo--round" style="left:240px;top:104px;width:78px;height:78px" role="img" aria-label="Round photo of a clinical skills workshop"></div>
  <div class="photo photo--round" style="left:378px;top:240px;width:112px;height:112px" role="img" aria-label="Round photo of a speaker at the podium"></div>

  <h1 class="front-headline">SAVE<br>THE DATE</h1>
  <p class="front-date">JUNE, from 1st - 4th</p>
  <p class="tagline front-tagline">STRONGER UNITED:<strong>Gather. Spark. Flourish.</strong></p>

  <p class="vision">Vision: The vision of the DORV 2020 conference is to improve patient care by bringing together the Canadian Emergency Medicine community.</p>
  <p class="url front-url"><span class="dot"></span>www.dorvsummit.ca</p>
  <div class="logo front-logo"><span class="mark"></span>DORV2020</div>
</section>

<section class="postcard postcard--back" aria-label="Postcard back">
  <div class="photo photo--lab" role="img" aria-label="Photo of delegates practising on a training mannequin"></div>
  <svg class="shapes" width="656" height="469" viewBox="0 0 656 469" aria-hidden="true">
    <defs>
      <linearGradient id="backStripe" x1="0" y1="0" x2="1" y2="0">
        <stop offset="0" stop-color="#1f5fae"/>
        <stop offset="1" stop-color="#7b2f9e"/>
      </linearGradient>
    </defs>
    <polygon points="330,0 430,0 360,230 330,230" fill="#ffffff"/>
    <polygon points="400,0 440,0 372,230 344,230" fill="#e4e4ea"/>
    <polygon points="0,190 345,190 330,230 0,230" fill="url(#backStripe)"/>
    <polygon points="330,230 345,190 345,358 330,358" fill="#0a1e44"/>
  </svg>
  <div class="photo photo--round" style="left:346px;top:114px;width:96px;height:96px" role="img" aria-label="Round photo of the riverside city view"></div>
  <div class="logo back-logo"><span class="mark"></span>DORV2020</div>

  <div class="objectives">
    <h2>LEARNING OBJECTIVES:</h2>
    <p>By the end of the conference, delegates will be able to:</p>
    <ul>
      <li>Apply up to date evidence to inform clinical decisions</li>
      <li>Acquire practical skills by participating in interactive sessions</li>
      <li>Connect and collaborate with other delegates</li>
      <li>Consider strategies to ensure career longevity</li>
      <li>Influence the future direction of Emergency Medicine in Canada</li>
    </ul>
  </div>

  <div class="back-info">
    <p class="back-tagline">STRONGER UNITED: Gather. Spark. Flourish.</p>
    <p class="back-date">JUNE, from 1st - 4th</p>
  </div>
  <p class="back-url-band"><span class="dot"></span>www.dorvsummit.ca</p>
</section>

</body>
</html>
```